Business card design for global fintech startup

Verdell is a modern payments platform for the global insurance industry, serving international health, life, and travel insurers, MGAs, brokers, and partners.

We need a professional, premium business card for use at insurance conferences and executive meetings. The goal is to create a card that feels trustworthy, modern, and high-quality, while still being distinctive and memorable in a stack of business cards.

Target audience:
Senior insurance executives (VP, C-suite).

Design goals:
Clear, professional, and credible
Modern but not trendy
Premium and well-structured
Easy to read and practical for networking

Brand direction:
Brand-first (company over individual)
Follow existing brand guidelines where possible
Clean layout, strong hierarchy, excellent readability

Must include:
Name
Title
Company name (Verdell)
Logo
Email
Phone/Whatsapp
Website (www.joinverdell.com)
Tagline - Payments Built On Trust

Materials & finish:
Open to designer recommendations for premium look and feel.

Please avoid:
Flashy or trendy startup styles
Generic insurance icons or clichés
Cluttered layouts or hard-to-read text

Deliverables:
Front and back business card, print-ready files.

Target Market(s)

Global Insurance executives

Industry/Entity Type

Fintech, Insurtech, Insurance, Financial Services

Contact Information for Business Card

Name Title Company name (Verdell) Logo Email Phone/Whatsapp Website (www.joinverdell.com) Tagline - Payments Built On Trust

Font styles to use
Other font styles liked:
• See brand guidelines

Requirements
Nice to have
• something that stands out/makes us more memorable while still remaining professional
Should not have
• Please avoid: Flashy or trendy startup styles Generic insurance icons or clichés Cluttered layouts or hard-to-read text

```html
<!DOCTYPE html>
<html lang="en">
<head>
<meta charset="utf-8">
<title>Verdell Business Cards</title>
<link rel="stylesheet" href="https://fonts.googleapis.com/css2?family=Ubuntu:wght@400;500;700&family=Work+Sans:wght@400;500;600&display=swap">
<style>
  :root{
    --page:#e9e6e1;
    --card:#ffffff;
    --ink:#1d1d1f;
    --band:#1f1f21;
    --orange:#f07a22;
    --gold:#f2bd4e;
    --blue:#3b86c9;
    --purple:#5b3fa0;
    --rule:#b9b9b9;
    --faint:#e7eef7;
    --sky:#a6e2f3;
    --peach:#fde3cc;
  }
  *{box-sizing:border-box;margin:0;padding:0}
  html,body{width:1200px;height:995px;overflow:hidden;background:var(--page)}
  .sheet{position:relative;width:1200px;height:995px}
  .card{position:absolute;width:540px;height:310px;border-radius:28px;background:var(--card);overflow:hidden;box-shadow:0 8px 22px rgba(0,0,0,.18)}
  .card--front{left:40px;top:140px}
  .card--back-wide{left:620px;top:140px}
  .card--back-gradient{left:40px;top:545px;background:linear-gradient(110deg,var(--sky) 0%,#e6f4f6 48%,var(--peach) 100%)}
  .card--back-white{left:620px;top:545px}

  /* front */
  .wordmark{position:absolute;left:34px;top:40px;display:flex;align-items:center;gap:12px;font-family:"Ubuntu",sans-serif;font-weight:500;font-size:40px;letter-spacing:3px;color:var(--ink)}
  .wordmark__dot{width:22px;height:22px;border-radius:50%;background:var(--orange)}
  .faint-mark{position:absolute;right:36px;top:34px;font-family:"Ubuntu",sans-serif;font-weight:500;font-size:50px;color:var(--faint)}
  .person{position:absolute;right:36px;top:118px;text-align:right;font-family:"Work Sans",sans-serif;color:var(--blue)}
  .person__name{font-weight:600;font-size:22px;letter-spacing:.5px}
  .person__title{font-size:14px}
  .contacts{position:absolute;left:34px;top:140px;list-style:none;font-family:"Work Sans",sans-serif;font-size:14px;color:var(--ink)}
  .contacts li{display:flex;align-items:center;gap:8px;height:24px}
  .contacts svg{width:14px;height:14px;flex:none}
  .band{position:absolute;left:0;top:0}
  .band__tagline{position:absolute;left:262px;top:262px;font-family:"Work Sans",sans-serif;font-weight:600;font-size:19px;color:var(--gold);white-space:nowrap}

  /* backs */
  .mark{font-family:"Ubuntu",sans-serif;font-weight:500;color:var(--ink);display:flex;align-items:center}
  .mark__dot{border-radius:50%;background:var(--orange)}
  .tagline{font-family:"Ubuntu",sans-serif;font-weight:500;color:var(--ink);line-height:1.1}
  .site{font-family:"Ubuntu",sans-serif;color:var(--ink);letter-spacing:2px}
  .site__domain{color:var(--purple)}

  .card--back-wide .mark{position:absolute;left:0;right:0;top:58px;justify-content:center;gap:10px;font-size:30px}
  .card--back-wide .mark__dot{width:18px;height:18px}
  .card--back-wide .tagline{position:absolute;left:0;right:0;top:120px;text-align:center;font-size:42px;white-space:nowrap}
  .card--back-wide .site{position:absolute;left:0;right:0;top:210px;text-align:center;font-size:18px}

  .card--back-gradient .mark,.card--back-white .mark{position:absolute;left:36px;top:126px;gap:12px;font-size:46px}
  .card--back-gradient .mark__dot,.card--back-white .mark__dot{width:26px;height:26px}
  .stack{position:absolute;left:286px;top:78px;width:228px}
  .stack .tagline{font-size:32px;white-space:nowrap}
  .stack__rule{height:1px;background:var(--rule);margin:16px 0 14px}
  .stack .site{font-size:15px;white-space:nowrap}
</style>
</head>
<body>
<main class="sheet">

  <section class="card card--front" aria-label="Card front">
    <div class="faint-mark" aria-hidden="true">Verdell</div>
    <div class="wordmark"><span class="wordmark__dot"></span>VERDELL</div>
    <div class="person">
      <p class="person__name">MARA ELLISON</p>
      <p class="person__title">Owner</p>
    </div>
    <ul class="contacts">
      <li><svg viewBox="0 0 16 16"><path d="M4 1l3 3-2 2c1 2 3 4 5 5l2-2 3 3-2 3C7 15 1 9 1 3z" fill="var(--ink)"/></svg>555.210.4830</li>
      <li><svg viewBox="0 0 16 16"><circle cx="8" cy="8" r="6.5" fill="none" stroke="var(--ink)" stroke-width="1.6"/></svg>555.318.6042</li>
      <li><svg viewBox="0 0 16 16"><rect x="1" y="3" width="14" height="10" rx="1" fill="var(--ink)"/><path d="M1 4l7 5 7-5" fill="none" stroke="#fff" stroke-width="1.2"/></svg>info@joinverdell.com</li>
      <li><svg viewBox="0 0 16 16" fill="none" stroke="var(--ink)" stroke-width="1.2"><circle cx="8" cy="8" r="6.5"/><ellipse cx="8" cy="8" rx="3" ry="6.5"/><path d="M1.5 8h13"/></svg>www.joinverdell.com</li>
    </ul>
    <svg class="band" width="540" height="310" viewBox="0 0 540 310" aria-hidden="true">
      <polygon points="0,266 224,266 217,282 0,282" fill="var(--orange)"/>
      <polygon points="0,292 220,292 247,240 540,240 540,310 0,310" fill="var(--band)"/>
    </svg>
    <p class="band__tagline">Payments Built On Trust</p>
  </section>

  <section class="card card--back-wide" aria-label="Card back, centred">
    <div class="mark"><span class="mark__dot"></span>Verdell</div>
    <p class="tagline">Payments Built On Trust</p>
    <p class="site">www.<span class="site__domain">joinverdell</span>.com</p>
  </section>

  <section class="card card--back-gradient" aria-label="Card back, gradient">
    <div class="mark"><span class="mark__dot"></span>Verdell</div>
    <div class="stack">
      <p class="tagline">Payments Built<br>On Trust</p>
      <div class="stack__rule"></div>
      <p class="site">www.<span class="site__domain">joinverdell</span>.com</p>
    </div>
  </section>

  <section class="card card--back-white" aria-label="Card back, white">
    <div class="mark"><span class="mark__dot"></span>Verdell</div>
    <div class="stack">
      <p class="tagline">Payments Built<br>On Trust</p>
      <div class="stack__rule"></div>
      <p class="site">www.<span class="site__domain">joinverdell</span>.com</p>
    </div>
  </section>

</main>
</body>
</html>
```